Redesign the Eshop of a gift shop

We want to redesign the front page, the category page and the product page of our Eshop that sells gifts.
I am thinking not to reveal the url of the eshop as i don't want you to get influenced. Lets call the Eshop "PresentNest.com"
I will list the brands that we resell so you understand what we are selling,
Morvato-https://www.morvato-example.com/
Zandorpel-https://zandorpel-example.com/
Vamtol - https://vamtol-example.com/
Quiet Orchard - https://www.quietorchard-example.com/
Ranger's Workbench - https://rangersworkbench-example.com/
Plumeline press - https://plumelinepress-example.com/
Tarpawn - https://tarpawnofficial-example.com/
We also sell toys for adults like backgamon, chess, playing cards, board games.
The problem is that many eshops sell these and thats why i would like the design to have a different approach, more fresh, not seen before.
I am also thinking of something playfull, happy, but warm at the same time.
Please note that our logo is black & white but feel free to play with any color/s you like in your website design. We might eventually even adjust the logo colors, or you can provide a pallete that suites a black and white logo
Let me know if you have any questions!
Updates
A couple of designers kindly asked to extend so they can submit.
Target Market(s)
Age: 20-50, Gender: Also men but mostly women, Income: Moderate to high, Interests and Lifestyle: Customers who value sentimentality, personal connection, and thoughtful gestures, Relationship Status: Those in relationships or with larger families
Number of Pages Required
3 page
Look and feel
Each slider illustrates characteristics of the customer's brand and the style your logo design should communicate.

```html
<!DOCTYPE html>
<html lang="en">
<head>
<meta charset="utf-8">
<title>PresentNest – Gifts Shop</title>
<link href="https://fonts.googleapis.com/css2?family=Poppins:wght@300;400;500;600;700;800&display=swap" rel="stylesheet">
<style>
:root{
  --orange:#f7941d;
  --cyan:#00b9e8;
  --ink:#1f1f1f;
  --muted:#555;
  --line:#e7e7e7;
  --panel:#f1f1f1;
  --band:#f3f4f6;
  --pink:#d98a95;
}
*{box-sizing:border-box;margin:0;padding:0}
html,body{width:1200px;height:2415px;overflow:hidden;background:#fff}
body{font-family:'Poppins',sans-serif;color:var(--ink);position:relative}
.abs{position:absolute}
.topline{left:0;top:0;width:1200px;height:9px;background:#eef3f4}
.foot-band{left:0;top:2038px;width:1200px;height:377px;background:var(--band)}
a{color:inherit;text-decoration:none}

/* header */
.toplinks{top:26px;left:742px;display:flex;gap:10px;font-size:9.5px;color:#444;align-items:center}
.toplinks .sep{width:1px;height:10px;background:#ccc}
.toplinks .drop::after{content:"";display:inline-block;margin-left:7px;border:4px solid transparent;border-top:5px solid #222;border-bottom:0;vertical-align:middle}
.brand{display:flex;align-items:center;gap:6px;font-weight:300;font-size:17px;letter-spacing:1px;color:#111;white-space:nowrap}
.brand .mark{width:12px;height:12px;background:#111}
.header-brand{left:162px;top:58px}
.sale-pill{left:322px;top:58px;width:231px;height:24px;border-radius:12px;background:var(--orange);color:#fff;font-size:10.5px;font-weight:600;display:flex;align-items:center;padding-left:12px;gap:4px;white-space:nowrap}
.sale-pill .dot{background:#ee1ecf;border-radius:50%;width:30px;height:30px;display:flex;align-items:center;justify-content:center}
.search{left:589px;top:56px;width:213px;height:28px;background:#f4f4f4;border-radius:3px;font-size:9px;color:#aaa;padding:8px 10px}
.search .btn{position:absolute;right:0;top:0;width:28px;height:28px;background:var(--orange);border-radius:0 3px 3px 0;display:flex;align-items:center;justify-content:center}
.hicon{top:62px;display:flex;align-items:center;gap:6px;font-size:9.5px;color:#333}
.hicon .badge{position:absolute;top:-4px;left:14px;font-size:7px}

/* nav */
.tab{top:110px;height:54px;background:#fff;border-radius:8px;box-shadow:0 2px 8px rgba(0,0,0,.07);font-size:10.5px;letter-spacing:.4px;display:flex;flex-direction:column;align-items:center;justify-content:center;gap:4px}
.tab::after{content:"";border:3px solid transparent;border-top:4px solid var(--orange)}

/* promo tiles */
.tile{border-radius:8px;overflow:hidden;background:var(--panel)}
.ph{position:absolute;border-radius:6px}
.shop{color:var(--cyan);font-weight:700;font-size:11px;display:flex;align-items:center;gap:6px}
.shop::after{content:"";width:5px;height:5px;border-right:2px solid currentColor;border-top:2px solid currentColor;transform:rotate(45deg)}
.sale-badge{width:56px;height:56px;border-radius:50%;background:#fff;box-shadow:0 2px 6px rgba(0,0,0,.08);display:flex;flex-direction:column;align-items:center;justify-content:center;transform:rotate(-18deg);line-height:1}
.sale-badge b{color:var(--cyan);font-size:11px}
.sale-badge i{font-style:normal;color:var(--cyan);font-size:16px;font-weight:300}
.sale-badge s{text-decoration:none;font-size:10px;font-weight:700}

/* sections */
.sec-head{left:162px;width:875px;display:flex;align-items:center;justify-content:space-between}
.sec-head h2{font-size:19px;font-weight:600;display:flex;align-items:center;gap:12px}
.view-all{font-size:11px;display:flex;align-items:center;gap:10px}
.view-all::after{content:"";width:5px;height:5px;border-right:2px solid var(--cyan);border-top:2px solid var(--cyan);transform:rotate(45deg)}
.card{width:208px;height:270px;background:#fff;border-radius:6px;box-shadow:0 2px 10px rgba(0,0,0,.08)}
.card .img{position:absolute;left:50%;transform:translateX(-50%)}
.card .name{position:absolute;top:160px;left:10px;right:10px;text-align:center;font-size:10px;line-height:14px;color:#333}
.card .price{position:absolute;top:203px;width:100%;text-align:center;color:var(--orange);font-weight:600;font-size:11.5px}
.card .stars{position:absolute;left:10px;top:238px;display:flex;gap:2px}
.card .rev{position:absolute;left:10px;top:255px;font-size:7px}
.card .cart{position:absolute;right:6px;top:234px;width:93px;height:29px;border:1.5px solid var(--cyan);border-radius:6px;font-size:10px;display:flex;align-items:center;justify-content:center;gap:5px}
.arrow{width:16px;height:16px;border-radius:50%;display:flex;align-items:center;justify-content:center}
.arrow.off{background:#cfcfcf}
.arrow.on{background:var(--cyan)}

/* features */
.feature{top:1818px;display:flex;align-items:center;gap:12px;font-weight:600;font-size:14px}

/* newsletter */
.news{left:162px;top:1898px;width:875px;height:243px;border-radius:8px;background:var(--cyan);color:#fff;text-align:center}
.news h3{position:absolute;top:84px;width:100%;font-weight:300;font-size:34px}
.news p{position:absolute;top:131px;width:100%;font-size:11.5px}
.news .field{position:absolute;left:272px;top:166px;width:333px;height:27px;background:#fff;border-radius:3px;color:#999;font-size:9.5px;text-align:left;padding:7px 11px}

/* footer */
.fcol{display:flex;flex-direction:column;gap:8.5px;font-size:10.5px;letter-spacing:.4px;color:#222}
.about{left:162px;top:2245px;width:225px;font-size:8px;line-height:12.5px;color:#333}
.pay{width:26px;height:16px;border-radius:2px}
</style>
</head>
<body>
<svg width="0" height="0" style="position:absolute">
  <defs>
    <symbol id="star" viewBox="0 0 10 10"><path d="M5 .5l1.4 2.9 3.1.4-2.3 2.2.6 3.1L5 7.6 2.2 9.1l.6-3.1L.5 3.8l3.1-.4z" fill="#f9b800"/></symbol>
    <symbol id="bag" viewBox="0 0 14 14"><path d="M2.5 4.5h9l-.8 8h-7.4z M5 4.5V3a2 2 0 014 0v1.5" fill="none" stroke="#f7941d" stroke-width="1.3"/></symbol>
    <symbol id="gift" viewBox="0 0 22 22"><rect x="2" y="8" width="18" height="4" fill="none" stroke="#00b9e8" stroke-width="1.5"/><rect x="4" y="12" width="14" height="8" fill="none" stroke="#00b9e8" stroke-width="1.5"/><path d="M11 8v12M11 8C8 3 5 4 6.5 7.5M11 8c3-5 6-4 4.5-.5" fill="none" stroke="#00b9e8" stroke-width="1.5"/></symbol>
    <symbol id="chev" viewBox="0 0 10 10"><path d="M4 2.5L6.5 5 4 7.5" fill="none" stroke="#fff" stroke-width="1.5"/></symbol>
  </defs>
</svg>

<div class="abs topline"></div>
<div class="abs foot-band"></div>

<!-- header -->
<div class="abs toplinks"><a>About Us</a><span class="sep"></span><a>Contact</a><span class="sep"></span><a>Return policy</a><span style="width:14px"></span><a class="drop">USD</a><span style="width:4px"></span><a class="drop">Eng</a></div>
<div class="abs brand header-brand"><span class="mark"></span>PRESENTNEST</div>
<div class="abs sale-pill">Summer Season Sale Up To <span class="dot">25%</span> OFF</div>
<div class="abs search">Search item<span class="btn"><svg width="13" height="13" viewBox="0 0 14 14"><circle cx="6" cy="6" r="4.2" fill="none" stroke="#fff" stroke-width="1.6"/><path d="M9 9l3.5 3.5" stroke="#fff" stroke-width="1.6"/></svg></span></div>
<div class="abs hicon" style="left:824px"><svg width="20" height="18" viewBox="0 0 20 18"><path d="M10 16S2 11 2 6a4 4 0 018-1 4 4 0 018 1c0 5-8 10-8 10z" fill="none" stroke="#f7941d" stroke-width="1.5"/></svg><span class="badge">0</span>Wishlist</div>
<div class="abs hicon" style="left:903px"><svg width="18" height="18"><use href="#bag"/></svg><span class="badge">0</span>Cart</div>
<div class="abs toplinks" style="left:965px;top:65px"><a class="drop">My Account</a></div>

<!-- nav -->
<div class="abs tab" style="left:162px;width:59px">Toys</div>
<div class="abs tab" style="left:229px;width:73px">Fashion</div>
<div class="abs tab" style="left:309px;width:75px">Outdoor</div>
<div class="abs tab" style="left:392px;width:97px">Accessories</div>
<div class="abs tab" style="left:498px;width:97px">New Arrivals</div>
<div class="abs tab" style="left:603px;width:81px">Hot Deals</div>
<div class="abs tab" style="left:691px;width:65px">More</div>

<!-- hero -->
<div class="abs tile" style="left:162px;top:179px;width:594px;height:320px;background:linear-gradient(120deg,#ececec,#f7f7f7)">
  <div class="ph" role="img" aria-label="Patterned tote bags on a white cushion" style="left:42px;top:30px;width:270px;height:260px;background:radial-gradient(ellipse at 45% 55%,#c89a6b,#4aa0b0 45%,#e4e4e4 72%)"></div>
  <div class="abs" style="left:315px;top:90px;font-size:33px;font-weight:300;line-height:1">Best <span style="color:var(--orange)">Summer</span></div>
  <div class="abs" style="left:314px;top:122px;font-size:45px;font-weight:300;color:var(--orange);line-height:1.05">Collections</div>
  <div class="abs" style="left:315px;top:166px;font-size:22px;font-weight:600">Just Arrived</div>
  <div class="abs shop" style="left:343px;top:222px;font-size:16px;letter-spacing:1px">Shop Now</div>
  <div class="abs arrow off" style="left:8px;top:152px"><svg width="10" height="10" style="transform:scaleX(-1)"><use href="#chev"/></svg></div>
  <div class="abs arrow" style="left:568px;top:152px;background:#777"><svg width="10" height="10"><use href="#chev"/></svg></div>
</div>

<div class="abs tile" style="left:767px;top:110px;width:270px;height:188px;background:linear-gradient(90deg,#d9cfc6,#efefef 45%)">
  <div class="ph" role="img" aria-label="Child hugging a green plush dinosaur" style="left:0;top:0;width:125px;height:188px;background:linear-gradient(160deg,#cbb6a6,#9bc27a 60%,#d8cdc2)"></div>
  <div class="abs sale-badge" style="left:200px;top:12px"><b>SALE</b><i>45%</i><s>OFF</s></div>
  <div class="abs" style="left:126px;top:57px;font-size:17px;font-weight:300">Gifts for</div>
  <div class="abs" style="left:126px;top:70px;font-size:52px;font-weight:800;color:var(--orange);line-height:1.1">Kids</div>
  <div class="abs" style="left:126px;top:126px;font-size:17px">Toys . Games</div>
  <div class="abs shop" style="left:180px;top:163px">Shop Now</div>
</div>

<div class="abs tile" style="left:767px;top:310px;width:270px;height:189px;background:linear-gradient(90deg,#f0f0f0 50%,#e5dcd6)">
  <div class="ph" role="img" aria-label="Smiling woman holding a game box" style="left:135px;top:0;width:135px;height:189px;background:linear-gradient(200deg,#4a3a34,#e7c9b6 50%,#f3e6dd)"></div>
  <div class="abs sale-badge" style="left:14px;top:8px"><b>SALE</b><i>45%</i><s>OFF</s></div>
  <div class="abs" style="left:18px;top:70px;font-size:17px;font-weight:300">Games for</div>
  <div class="abs" style="left:18px;top:86px;font-size:38px;font-weight:800;color:var(--orange);line-height:1.1">Adults</div>
  <div class="abs" style="left:18px;top:134px;font-size:10px;letter-spacing:.3px">Backgamon . Chess . Cards . Board</div>
  <div class="abs shop" style="left:20px;top:162px">Shop Now</div>
</div>

<div class="abs tile" style="left:162px;top:508px;width:271px;height:188px">
  <div class="ph" role="img" aria-label="Blue star-print zip pouch" style="left:8px;top:58px;width:100px;height:78px;background:linear-gradient(135deg,#2a78c8,#6fb0e8)"></div>
  <div class="abs" style="left:125px;top:68px;font-size:34px;font-weight:300;color:var(--orange);line-height:1">Fashion</div>
  <div class="abs" style="left:125px;top:101px;font-size:17px;font-weight:300">Collection</div>
  <div class="abs shop" style="left:177px;top:158px">Shop Now</div>
</div>

<div class="abs tile" style="left:443px;top:508px;width:594px;height:188px">
  <div class="ph" role="img" aria-label="Boxed outdoor gadgets: fire starter, garden hydrometer and tool set" style="left:50px;top:40px;width:190px;height:122px;background:linear-gradient(90deg,#4a4a4a,#c46a4a 45%,#3b6e4a)"></div>
  <div class="abs" style="left:339px;top:52px;font-size:32px;font-weight:300;color:var(--orange);line-height:30px">Outdoor &amp;<br>Accessories</div>
  <div class="abs" style="left:339px;top:114px;font-size:17px;font-weight:300;line-height:1.2">Collection</div>
  <div class="abs shop" style="left:340px;top:158px">Shop Now</div>
</div>

<!-- most popular -->
<div class="abs sec-head" style="top:762px"><h2><svg width="22" height="22"><use href="#gift"/></svg>Most Popular</h2><span class="view-all">View All</span></div>
<div class="abs arrow off" style="left:131px;top:938px"><svg width="10" height="10" style="transform:scaleX(-1)"><use href="#chev"/></svg></div>
<div class="abs arrow on" style="left:1053px;top:938px"><svg width="10" height="10"><use href="#chev"/></svg></div>

<div class="abs card" style="left:162px;top:812px">
  <div class="img" role="img" aria-label="Floral beach ball" style="top:12px;width:110px;height:110px;border-radius:50%;background:radial-gradient(circle at 60% 45%,#f06a5a,#f5d3cb 50%,#e9efe6)"></div>
  <div class="name">Pallone da Spiaggia Soffice<br>- Sole Vivo</div><div class="price">$9.95</div>
  <div class="stars"><svg width="11" height="11"><use href="#star"/></svg><svg width="11" height="11"><use href="#star"/></svg><svg width="11" height="11"><use href="#star"/></svg><svg width="11" height="11"><use href="#star"/></svg><svg width="11" height="11"><use href="#star"/></svg></div>
  <div class="rev">105 reviews</div><div class="cart"><svg width="13" height="13"><use href="#bag"/></svg>Add to Cart</div>
</div>
<div class="abs card" style="left:384px;top:812px">
  <div class="img" role="img" aria-label="Illustrated travel journal cover" style="top:16px;width:72px;height:108px;border-radius:2px;background:linear-gradient(160deg,#7ea3a8,#c8a45a)"></div>
  <div class="name">Halverson Design Journal<br>- Santorini</div><div class="price">$9.95</div>
  <div class="stars"><svg width="11" height="11"><use href="#star"/></svg><svg width="11" height="11"><use href="#star"/></svg><svg width="11" height="11"><use href="#star"/></svg><svg width="11" height="11"><use href="#star"/></svg><svg width="11" height="11"><use href="#star"/></svg></div>
  <div class="rev">105 reviews</div><div class="cart"><svg width="13" height="13"><use href="#bag"/></svg>Add to Cart</div>
</div>
<div class="abs card" style="left:607px;top:812px">
  <div class="img" role="img" aria-label="Weather house hygrometer kit box" style="top:14px;width:112px;height:118px;border-radius:2px;background:linear-gradient(180deg,#f2f2f2 20%,#8fc0e0 45%,#d9552c 75%,#5a9a4a)"></div>
  <div class="name">Zandorpel DIY make your own<br>weather house- Hygrometer</div><div class="price">$19.95</div>
  <div class="stars"><svg width="11" height="11"><use href="#star"/></svg><svg width="11" height="11"><use href="#star"/></svg><svg width="11" height="11"><use href="#star"/></svg><svg width="11" height="11"><use href="#star"/></svg><svg width="11" height="11"><use href="#star"/></svg></div>
  <div class="rev">105 reviews</div><div class="cart"><svg width="13" height="13"><use href="#bag"/></svg>Add to Cart</div>
</div>
<div class="abs card" style="left:830px;top:812px">
  <div class="img" role="img" aria-label="Terracotta watering stake package" style="top:16px;width:88px;height:120px;border-radius:2px;background:linear-gradient(90deg,#e7e7e7 40%,#3f6b44)"></div>
  <div class="name">Zandorpel Self-watering slow release<br>state, indoor/outdoor.</div><div class="price">$9.95</div>
  <div class="stars"><svg width="11" height="11"><use href="#star"/></svg><svg width="11" height="11"><use href="#star"/></svg><svg width="11" height="11"><use href="#star"/></svg><svg width="11" height="11"><use href="#star"/></svg><svg width="11" height="11"><use href="#star"/></svg></div>
  <div class="rev">105 reviews</div><div class="cart"><svg width="13" height="13"><use href="#bag"/></svg>Add to Cart</div>
</div>

<!-- hot deals -->
<div class="abs tile" style="left:162px;top:1144px;width:875px;height:188px;background:var(--pink)">
  <div class="ph" role="img" aria-label="Happy shopper with bags holding a sale sign" style="left:160px;top:0;width:360px;height:188px;border-radius:0;background:linear-gradient(90deg,rgba(255,255,255,.5),#c9a08a 40%,#e0405a 70%,rgba(217,138,149,0))"></div>
  <div class="abs" style="left:30px;top:30px;width:104px;height:104px;border-radius:50%;border:2px solid rgba(255,255,255,.8);color:#fff;text-align:center;padding-top:26px;font-weight:300;font-size:18px;line-height:1.1">$<br>LOWEST<br><span style="letter-spacing:7px;font-size:15px">PRICE</span></div>
  <div class="abs" style="left:575px;top:54px;font-size:40px;font-weight:300;color:#fff;line-height:1">Hot Deals</div>
  <div class="abs" style="left:575px;top:96px;font-size:17px;font-weight:300;color:#fff">Summer SALE</div>
  <div class="abs shop" style="left:580px;top:137px;color:#fff">Shop Now</div>
</div>

<!-- new arrivals -->
<div class="abs sec-head" style="top:1395px"><h2><svg width="22" height="22"><use href="#gift"/></svg>New Arrivals</h2><span class="view-all">View All</span></div>
<div class="abs arrow off" style="left:131px;top:1571px"><svg width="10" height="10" style="transform:scaleX(-1)"><use href="#chev"/></svg></div>
<div class="abs arrow on" style="left:1053px;top:1571px"><svg width="10" height="10"><use href="#chev"/></svg></div>

<div class="abs card" style="left:162px;top:1444px">
  <div class="img" role="img" aria-label="Floral beach ball" style="top:12px;width:110px;height:110px;border-radius:50%;background:radial-gradient(circle at 60% 45%,#f06a5a,#f5d3cb 50%,#e9efe6)"></div>
  <div class="name">Pallone da Spiaggia Soffice<br>- Sole Vivo</div><div class="price">$9.95</div>
  <div class="stars"><svg width="11" height="11"><use href="#star"/></svg><svg width="11" height="11"><use href="#star"/></svg><svg width="11" height="11"><use href="#star"/></svg><svg width="11" height="11"><use href="#star"/></svg><svg width="11" height="11"><use href="#star"/></svg></div>
  <div class="rev">105 reviews</div><div class="cart"><svg width="13" height="13"><use href="#bag"/></svg>Add to Cart</div>
</div>
<div class="abs card" style="left:384px;top:1444px">
  <div class="img" role="img" aria-label="Illustrated travel journal cover" style="top:16px;width:72px;height:108px;border-radius:2px;background:linear-gradient(160deg,#7ea3a8,#c8a45a)"></div>
  <div class="name">Halverson Design Journal<br>- Santorini</div><div class="price">$9.95</div>
  <div class="stars"><svg width="11" height="11"><use href="#star"/></svg><svg width="11" height="11"><use href="#star"/></svg><svg width="11" height="11"><use href="#star"/></svg><svg width="11" height="11"><use href="#star"/></svg><svg width="11" height="11"><use href="#star"/></svg></div>
  <div class="rev">105 reviews</div><div class="cart"><svg width="13" height="13"><use href="#bag"/></svg>Add to Cart</div>
</div>
<div class="abs card" style="left:607px;top:1444px">
  <div class="img" role="img" aria-label="Weather house hygrometer kit box" style="top:14px;width:112px;height:118px;border-radius:2px;background:linear-gradient(180deg,#f2f2f2 20%,#8fc0e0 45%,#d9552c 75%,#5a9a4a)"></div>
  <div class="name">Zandorpel DIY make your own<br>weather house- Hygrometer</div><div class="price">$19.95</div>
  <div class="stars"><svg width="11" height="11"><use href="#star"/></svg><svg width="11" height="11"><use href="#star"/></svg><svg width="11" height="11"><use href="#star"/></svg><svg width="11" height="11"><use href="#star"/></svg><svg width="11" height="11"><use href="#star"/></svg></div>
  <div class="rev">105 reviews</div><div class="cart"><svg width="13" height="13"><use href="#bag"/></svg>Add to Cart</div>
</div>
<div class="abs card" style="left:830px;top:1444px">
  <div class="img" role="img" aria-label="Terracotta watering stake package" style="top:16px;width:88px;height:120px;border-radius:2px;background:linear-gradient(90deg,#e7e7e7 40%,#3f6b44)"></div>
  <div class="name">Zandorpel Self-watering slow release<br>state, indoor/outdoor.</div><div class="price">$9.95</div>
  <div class="stars"><svg width="11" height="11"><use href="#star"/></svg><svg width="11" height="11"><use href="#star"/></svg><svg width="11" height="11"><use href="#star"/></svg><svg width="11" height="11"><use href="#star"/></svg><svg width="11" height="11"><use href="#star"/></svg></div>
  <div class="rev">105 reviews</div><div class="cart"><svg width="13" height="13"><use href="#bag"/></svg>Add to Cart</div>
</div>

<!-- features -->
<div class="abs feature" style="left:191px"><svg width="30" height="24" viewBox="0 0 30 24"><rect x="1" y="3" width="17" height="14" rx="2" fill="#00b9e8"/><path d="M18 8h6l4 5v4H18z" fill="#00b9e8"/><circle cx="7" cy="19" r="3" fill="#00b9e8" stroke="#fff" stroke-width="1.5"/><circle cx="23" cy="19" r="3" fill="#00b9e8" stroke="#fff" stroke-width="1.5"/></svg>Free Shipping</div>
<div class="abs feature" style="left:413px"><svg width="30" height="22" viewBox="0 0 30 22"><rect x="0" y="1" width="30" height="20" rx="2" fill="#00b9e8"/><rect x="0" y="6" width="30" height="4" fill="#fff"/><rect x="4" y="14" width="8" height="3" fill="#fff"/></svg>Secure Payment</div>
<div class="abs feature" style="left:650px"><svg width="34" height="28" viewBox="0 0 34 28"><path d="M17 3a11 11 0 00-10 15l-2 7 7-2A11 11 0 1017 3z" fill="none" stroke="#00b9e8" stroke-width="2.2"/><circle cx="12" cy="14" r="1.8" fill="#00b9e8"/><circle cx="17" cy="14" r="1.8" fill="#00b9e8"/><circle cx="22" cy="14" r="1.8" fill="#00b9e8"/></svg>Support 24/7</div>
<div class="abs feature" style="left:876px"><svg width="28" height="28" viewBox="0 0 28 28"><circle cx="14" cy="14" r="13" fill="#00b9e8"/><path d="M17.5 10c-1-1.5-7-2-7 1s7 2 7 5-6 2.5-7.5 1M14 6v16" fill="none" stroke="#fff" stroke-width="1.8"/></svg>Lowest Price</div>

<!-- newsletter -->
<div class="abs news">
  <div class="ph" role="img" aria-label="Leather card wallet with aluminium card holder" style="left:60px;top:12px;width:210px;height:220px;background:linear-gradient(120deg,#9a9a9a,#222 60%,rgba(0,185,232,0))"></div>
  <div class="ph" role="img" aria-label="Navy enamel camping mug" style="left:655px;top:25px;width:140px;height:130px;border-radius:40%;background:radial-gradient(circle at 50% 45%,#2a5e8a,#1b2a5a 60%,rgba(0,185,232,0) 72%)"></div>
  <svg class="abs" style="left:421px;top:35px" width="34" height="34" viewBox="0 0 34 34"><path d="M3 13l14-10 14 10v18H3z" fill="none" stroke="#fff" stroke-width="1.6"/><rect x="8" y="7" width="18" height="16" fill="#00b9e8" stroke="#fff" stroke-width="1.6"/><circle cx="17" cy="15" r="4.5" fill="none" stroke="#fff" stroke-width="1.3"/><path d="M3 13l14 10 14-10" fill="none" stroke="#fff" stroke-width="1.6"/></svg>
  <h3>Newsletter</h3>
  <p>Signup and get up to date of our latest product and offers</p>
  <div class="field">Email Id<svg class="abs" style="right:9px;top:8px" width="12" height="12" viewBox="0 0 12 12"><path d="M1 5l10-4-4 10-1.5-4.5z" fill="#00b9e8"/></svg></div>
</div>

<!-- footer -->
<div class="abs brand" style="left:164px;top:2212px"><span class="mark"></span>PRESENTNEST</div>
<p class="abs about">Lorem ipsum dolor sit amet, consectetur adipiscing elit, sed do eiusmod tempor incididunt ut labore et dolore magna aliqua. Ut enim ad minim veniam, quis nostrud exercitation ullamco laboris nisi ut aliquip ex ea commodo consequat.</p>
<a class="abs" style="left:162px;top:2323px;font-size:8px;color:var(--cyan);font-weight:600">Read More About Us</a>
<div class="abs" style="left:162px;top:2373px;font-size:8px">© 2023 presentnest. All Right reserved.</div>

<div class="abs fcol" style="left:459px;top:2218px"><a>Toys</a><a>Fashion</a><a>Outdoor</a><a>Accessories</a><a>New Arrivals</a><a>Hot Deals</a><a>More</a></div>
<div class="abs fcol" style="left:595px;top:2218px"><a>kids</a><a>Fashion for Men</a><a>Fashion for Women</a><a>Offers</a><a>Shipping</a></div>
<div class="abs fcol" style="left:762px;top:2220px"><a>About Us</a><a>Contact</a><a>Return policy</a><a>Terms</a><a>Privacy policy</a></div>
<div class="abs fcol" style="left:909px;top:2219px;font-size:9px;gap:9px"><a>Wishlist <span style="font-size:7px;background:#e6e6e6;border-radius:50%;padding:1px 4px">0</span></a><a>My Account</a></div>
<div class="abs" style="left:909px;top:2285px;font-size:9px;color:var(--cyan);font-weight:600">Support</div>
<div class="abs" style="left:909px;top:2302px;font-size:11.5px;font-weight:600">+01 5550 246810</div>
<div class="abs" style="left:909px;top:2322px;font-size:9px;font-weight:500">hello@presentnest-example.com</div>
<div class="abs" style="left:909px;top:2347px;display:flex;gap:5px">
  <span class="pay" style="background:#1e3a8a"></span><span class="pay" style="background:#1a4fd8"></span><span class="pay" style="background:#1a1f71"></span><span class="pay" style="background:#2e8bdc"></span>
</div>
</body>
</html>
```